Different sized Banner ads for adult toystore. www.velvetlark.com.au

I need to design promotional banners to be used on signal harbor to send to sites such as glow nest. i would need the banner in different sizes. a couple of the designs should be pagecircle and clipzap ad freindly with no graphic content as to avoid being banned. make the ads Sleek, Sexy and cheeky and aimed at middle to upper class.. I need them in different sizes, vertical, horizontal and square similar to your ad. It is for online adult toy store in Australia. I can provide some images and I would like the banners promoting different products, some images are provided. classy and engaging. I would also like there to be an Australian owned element in the banner that has perhaps the Australian owned and made flag similar to the ones in your ad. the ads will be different to each other, some with just company logo some with products and some specifically for men, women, lgbt. attached are some files to work with, will be happy to provide more. catch phrases like "discreet delivery" are important. use the phrase "velvet lark, soft like satin" if possible.
include the website, www.velvetlark.com.au and an Australian made logo.
company logo and website must be present. will need designs to be suitable and catchy for platforms such as glow nest, different banner sizes including horizontal vertical large small and square. images are provided below for use. choose the best ones for the project. there is also a company logo with transparency to use.

Target Market(s)

Age range: The primary age range for the target audience typically falls between 25 to 45 years old. This group includes individuals who are young adults, working professionals, and those in their prime years. Gender: The target audience comprises both males and females. It's essential to cater to a diverse range of gender identities and sexual orientations, including LGBTQ+ individuals. Sexual orientation: The audience includes individuals of various sexual orientations, such as heterosexual, gay, lesbian, bisexual, and others within the LGBTQ+ spectrum. Relationship status: The target audience can consist of both singles and individuals in relationships. Singles may be looking to explore their sexuality and enhance their solo experiences, while those in relationships may seek ways to spice up their intimacy. Income level: The target audience may belong to middle to upper-class income levels. This group is more likely to have the disposable income to invest in higher-quality and more sophisticated adult toys and products. Education level: The target audience can include individuals with different levels of education, ranging from high school graduates to those with college degrees or higher. Location: The target audience can be spread across various regions of Australia, including urban centers and suburban areas. Interests: The audience may have diverse interests related to romance, self-care, self-love, wellness, and exploring their sexuality. Open-mindedness: The target audience should be open-minded, willing to embrace new experiences, and interested in exploring their desires and fantasies.

Industry/Entity Type

adult sex toys

Colors
0054AA
0677BA
7BADD7
CADEEF
E8F1F8
00AB8E
00BBA5
67D7C9
C6EFE9
E9F9F6
FFC000
F8CF3A
FAE287
FDF2CF
FEFAEE
F0912C
F2A743
F7CA91
FBE8D2
FDF5EE
A7469A
B969AE
D3A5CF
EDDBEB
F8F0F9
6B429C
8869AF
B7A5CE
E3DAEB
F3F0F8

Requirements
Must have
• Australian made and owned logo, company logo, website: www.velvetlark.com.au, call to action button e.g. "Shop Now", "Take a look" "Unlock your desires NOW", sleek and catchy design, enticing. One of the designs should simply be the black and with image of the girl (provided) with company logo and website, and the slogan "Unleash your desires"
Nice to have
• catchy slogan such as "unleash your desires with velvet lark", "Will beat any advertised price", "Velvet lark, soft like satin" "
Should not have
• black background, too many images

```html
<!DOCTYPE html>
<html lang="en">
<head>
<meta charset="utf-8">
<title>Velvet Lark – Vertical Banner</title>
<link rel="stylesheet" href="https://fonts.googleapis.com/css2?family=Nunito:wght@600;700;800&family=Cinzel:wght@500&display=swap">
<style>
  :root {
    --page-bg: #e6e6e6;
    --maroon: #42001c;
    --maroon-soft: #6a0030;
    --magenta: #e3196c;
    --blush: #f3b3c8;
    --photo-light: #f4d2cf;
    --photo-mid: #ecbcbc;
    --photo-pink: #ef7aa2;
    --photo-yellow: #f6d86a;
    --gold: #c08a00;
    --gold-text: #c9a055;
    --white: #ffffff;
  }
  * { margin: 0; padding: 0; box-sizing: border-box; }
  html, body {
    width: 952px; height: 1200px; overflow: hidden;
    background: var(--page-bg);
    font-family: "Nunito", sans-serif;
  }
  .banner {
    position: absolute; left: 211px; top: 41px;
    width: 530px; height: 1118px;
    background: var(--magenta);
    overflow: hidden;
  }
  .banner__shapes, .banner__photo {
    position: absolute; left: 0; top: 0; width: 530px; height: 1118px;
  }
  .brand {
    position: absolute; top: 42px; left: 0; width: 100%;
    text-align: center;
    font-family: "Cinzel", serif; font-weight: 500;
    font-size: 40px; letter-spacing: 4px;
    color: var(--gold-text);
  }
  .headline {
    position: absolute; top: 206px; left: 0; width: 100%;
    text-align: center; color: var(--white);
    font-weight: 800; font-size: 33px; line-height: 53px;
    text-transform: uppercase;
  }
  .features {
    position: absolute; top: 345px; left: 134px;
    list-style: none;
  }
  .feature {
    display: flex; align-items: center; gap: 15px;
    height: 50px; margin-bottom: 30px;
    color: var(--white); font-weight: 700; font-size: 24px;
  }
  .feature__icon {
    width: 50px; height: 50px; flex: none;
  }
  .cta {
    position: absolute; left: 146px; top: 990px;
    width: 224px; height: 70px;
    background: var(--gold); border-radius: 3px;
    color: var(--white); font-weight: 800; font-size: 21px;
    display: flex; align-items: center; justify-content: center;
    text-transform: uppercase;
  }
  .website {
    position: absolute; left: 0; top: 1068px; width: 100%;
    text-align: center; color: var(--white);
    font-weight: 600; font-size: 21px; letter-spacing: 4.5px;
  }
</style>
</head>
<body>
<main class="banner">
  <svg class="banner__shapes" viewBox="0 0 530 1118" aria-hidden="true">
    <path d="M0 0 H530 V118 C400 175 220 180 0 112 Z" fill="var(--maroon-soft)"/>
    <path d="M0 0 H530 V100 C400 155 220 160 0 100 Z" fill="var(--maroon)"/>
    <path d="M0 722 C130 630 310 575 530 592 V1118 H0 Z" fill="var(--blush)"/>
  </svg>

  <svg class="banner__photo" viewBox="0 0 530 1118" role="img" aria-label="Product photo: two hands holding a bunch of colourful pink, yellow, white and blue toys against a soft pink wall">
    <defs>
      <radialGradient id="photoTone" cx="260" cy="840" r="300" gradientUnits="userSpaceOnUse">
        <stop offset="0" stop-color="var(--photo-pink)"/>
        <stop offset="0.3" stop-color="var(--photo-yellow)" stop-opacity="0.85"/>
        <stop offset="0.6" stop-color="var(--photo-mid)"/>
        <stop offset="1" stop-color="var(--photo-light)"/>
      </radialGradient>
    </defs>
    <path d="M0 737 C130 648 310 594 530 608 V1027 H0 Z" fill="url(#photoTone)"/>
    <rect x="0" y="1027" width="530" height="91" fill="var(--maroon)"/>
  </svg>

  <div class="brand">VELVET LARK</div>

  <h1 class="headline">Unleash your desires<br>with Velvet Lark</h1>

  <ul class="features">
    <li class="feature">
      <svg class="feature__icon" viewBox="0 0 50 50" aria-hidden="true">
        <circle cx="25" cy="25" r="23" fill="var(--white)"/>
        <circle cx="25" cy="25" r="19" fill="none" stroke="var(--magenta)" stroke-width="2"/>
        <rect x="15" y="16" width="20" height="18" rx="2" fill="var(--magenta)"/>
        <rect x="15" y="21" width="20" height="2" fill="var(--white)"/>
        <rect x="21" y="25" width="8" height="5" fill="var(--white)"/>
      </svg>
      Discreet Delivery
    </li>
    <li class="feature">
      <svg class="feature__icon" viewBox="0 0 50 50" aria-hidden="true">
        <circle cx="25" cy="25" r="23" fill="var(--white)"/>
        <circle cx="25" cy="25" r="19" fill="none" stroke="var(--magenta)" stroke-width="2"/>
        <path d="M15 15 L35 35 M35 15 L15 35 M25 13 V37 M13 25 H37" stroke="var(--magenta)" stroke-width="3"/>
      </svg>
      Australian Made
    </li>
    <li class="feature">
      <svg class="feature__icon" viewBox="0 0 50 50" aria-hidden="true">
        <circle cx="25" cy="25" r="23" fill="var(--white)"/>
        <circle cx="25" cy="25" r="19" fill="none" stroke="var(--magenta)" stroke-width="2"/>
        <rect x="15" y="20" width="20" height="6" fill="var(--magenta)"/>
        <rect x="17" y="27" width="16" height="9" fill="var(--magenta)"/>
        <rect x="24" y="20" width="2" height="16" fill="var(--white)"/>
        <path d="M25 20 C21 13 16 17 22 20 M25 20 C29 13 34 17 28 20" fill="none" stroke="var(--magenta)" stroke-width="2"/>
      </svg>
      Free Gifts!
    </li>
  </ul>

  <div class="cta">Take a look</div>
  <div class="website">www.velvetlark.com.au</div>
</main>
</body>
</html>
```